Brantley Lawn Care. The best in the biz

I run a lawn care service that offers full service mowing. 100% satisfaction guarantee. Fast, Friendly, quality service "I am your lawns best friend" I cut residential lawns. I offer a mow package that includes trimming, edging and clean up. Prices very from 20 dollars to 75. I want my logo to stand out. Free estimates

Target Market(s)

Home owners

Industry/Entity Type

Landscaping

Contact Information for Business Card

555-612-4470 tidymow47@quillmail.example Dexter. Brantley Lawn care

Colors
f37122
9bcb3c
cadf82

Requirements
Must have
• Company name.
• Phone number
• Email
• My services
• images
Nice to have
• A sun that is growing grass.
Should not have
• Incorrect information

```html
<!DOCTYPE html>
<html lang="en">
<head>
<meta charset="utf-8">
<title>Brantley Lawn Care – Business Card</title>
<link rel="stylesheet" href="https://fonts.googleapis.com/css2?family=Source+Sans+3:wght@400;600&display=swap">
<style>
  :root {
    --backdrop: #3a3430;
    --card: #1a1a1a;
    --green: #1fae3c;
    --leaf: #9bcb3c;
    --yellow: #e8e21a;
    --title-yellow: #f2d21b;
    --orange: #f37122;
    --text: #e9e9e9;
    --divider: #5a5a5a;
  }
  * { box-sizing: border-box; margin: 0; padding: 0; }
  html, body {
    width: 1200px; height: 814px; overflow: hidden;
    background: var(--backdrop);
    font-family: "Source Sans 3", "Myriad Pro", sans-serif;
  }
  .canvas { position: relative; width: 1200px; height: 814px; }
  .card {
    position: absolute; top: 257px;
    width: 525px; height: 300px;
    background: var(--card);
    box-shadow: 0 6px 18px rgba(0,0,0,.45);
    overflow: hidden;
  }
  .card--front { left: 50px; }
  .card--back { left: 625px; }

  /* front */
  .brand-mark {
    position: absolute; left: 38px; top: 70px; width: 190px;
    display: flex; flex-direction: column; align-items: center; gap: 12px;
  }
  .brand-mark__dot {
    width: 76px; height: 76px; border-radius: 50%;
    background: var(--orange);
  }
  .brand-mark__name {
    font-weight: 600; font-size: 21px; color: var(--text); text-align: center; white-space: nowrap;
  }
  .divider {
    position: absolute; left: 255px; top: 40px; width: 1px; height: 120px;
    background: var(--divider);
  }
  .contact {
    position: absolute; left: 282px; top: 44px; right: 12px;
    color: var(--text); font-size: 15px; line-height: 1.35;
  }
  .contact__name { color: var(--green); font-size: 19px; font-weight: 600; line-height: 1.1; }
  .contact__title { color: var(--title-yellow); font-size: 15px; margin-bottom: 12px; }
  .contact__row { display: flex; align-items: center; gap: 7px; white-space: nowrap; }
  .contact__row svg { width: 13px; height: 13px; fill: var(--green); flex: none; }
  .services {
    position: absolute; left: 0; bottom: 0; width: 100%; height: 62px;
    background: var(--green);
    border-top: 3px solid var(--yellow);
    color: var(--yellow); font-size: 18px;
    display: flex; align-items: center; padding-left: 180px;
  }

  /* back */
  .back-name {
    position: absolute; inset: 0;
    display: flex; align-items: center; justify-content: center; gap: 14px;
  }
  .back-name__dot {
    width: 54px; height: 54px; border-radius: 50%; background: var(--orange); flex: none;
  }
  .back-name__text {
    color: var(--green); font-size: 32px; font-weight: 600; line-height: 1.05; white-space: nowrap;
  }
</style>
</head>
<body>
<main class="canvas">
  <section class="card card--front">
    <div class="brand-mark">
      <span class="brand-mark__dot"></span>
      <span class="brand-mark__name">Brantley Lawn Care</span>
    </div>
    <span class="divider"></span>
    <div class="contact">
      <p class="contact__name">Dale Merritt</p>
      <p class="contact__title">CEO/Founder</p>
      <p>Dexter. Brantley Lawn care</p>
      <p class="contact__row">
        <svg viewBox="0 0 24 24" aria-hidden="true"><path d="M6.6 10.8a15.1 15.1 0 0 0 6.6 6.6l2.2-2.2a1 1 0 0 1 1-.25 11.4 11.4 0 0 0 3.6.57 1 1 0 0 1 1 1V20a1 1 0 0 1-1 1A17 17 0 0 1 3 4a1 1 0 0 1 1-1h3.5a1 1 0 0 1 1 1c0 1.25.2 2.45.57 3.6a1 1 0 0 1-.25 1z"/></svg>
        555-612-4470
      </p>
      <p class="contact__row">
        <svg viewBox="0 0 24 24" aria-hidden="true"><path d="M2 5h20v14H2z M2 5l10 8 10-8" stroke="#1a1a1a" stroke-width="1.6"/></svg>
        tidymow47@quillmail.example
      </p>
    </div>
    <div class="services">Trimming • edging • clean up</div>
  </section>

  <section class="card card--back">
    <div class="back-name">
      <span class="back-name__dot"></span>
      <span class="back-name__text">Brantley Lawn Care</span>
    </div>
  </section>
</main>
</body>
</html>
```